Online-Marketing Material für Alltagsbegleiter
Zielgruppe
Wir bieten Haushaltshilfen und Alltagsbegleiter für Privathaushalte an. Unsere Hauptkundenklientel sind Pflegebedürftige Menschen denen eine Haushaltshilfe von der Pflegekasse zusteht. Weitere Kunden sind Familien und/oder Singlehaushalte, die eine Haushaltfshilfe benötigen.
Aufgabenstellung
Es soll ein neues Titelbild für unsere Facebokseite erstellt werden. Das Titelbild soll unser Logo enthalten und ggfls. auch ein paar Schrftzüge, bzw. Texte von unserer Internetseite. Das Titelbild soll leicht, locker und modern rüber kommen.

```html
<!DOCTYPE html>
<html lang="de">
<head>
<meta charset="utf-8">
<title>Sonnhaus – Titelbild</title>
<link rel="stylesheet" href="https://fonts.googleapis.com/css2?family=Arimo:wght@400;700&display=swap">
<style>
  :root {
    --brand-red: #c01e2e;
    --rose: #d56a86;
    --rose-deep: #c2354e;
    --cream: #f3e9e2;
    --peach: #e9c3b0;
    --ink: #353535;
    --white: #ffffff;
  }
  html, body {
    margin: 0;
    padding: 0;
    width: 1200px;
    height: 676px;
    overflow: hidden;
  }
  .cover {
    position: relative;
    width: 1200px;
    height: 676px;
    overflow: hidden;
    font-family: "Arimo", Arial, sans-serif;
    color: var(--white);
  }
  .cover__photo {
    position: absolute;
    inset: 0;
    background:
      radial-gradient(ellipse 420px 140px at 560px 300px, rgba(233,190,170,0.9), rgba(233,190,170,0) 70%),
      linear-gradient(90deg, rgba(170,170,178,0.75) 0%, rgba(170,170,178,0) 32%, rgba(0,0,0,0) 68%, rgba(232,150,40,0.85) 80%, rgba(232,150,40,0.9) 100%),
      linear-gradient(180deg, var(--cream) 0%, var(--peach) 40%, var(--rose) 70%, var(--rose-deep) 100%);
  }
  .cover__topbar {
    position: absolute;
    top: 0; left: 0; right: 0;
    height: 11px;
    background: var(--brand-red);
  }
  .cover__shade {
    position: absolute;
    left: 0; right: 0; bottom: 0;
    height: 330px;
    background: linear-gradient(180deg, rgba(200,60,90,0) 0%, rgba(205,70,100,0.55) 45%, rgba(192,30,46,0.85) 100%);
  }
  .brand {
    position: absolute;
    top: 82px;
    left: 0; right: 0;
    display: flex;
    justify-content: center;
    align-items: center;
    gap: 22px;
  }
  .brand__dot {
    width: 92px;
    height: 92px;
    border-radius: 50%;
    background: var(--brand-red);
  }
  .brand__name {
    font-weight: 700;
    font-size: 54px;
    letter-spacing: 2px;
    color: var(--ink);
  }
  .features {
    position: absolute;
    top: 416px;
    left: 0; right: 0;
    height: 120px;
  }
  .feature {
    position: absolute;
    top: 0;
    width: 220px;
    margin-left: -110px;
    text-align: center;
  }
  .feature__icon {
    display: block;
    margin: 0 auto;
    width: 62px;
    height: 58px;
  }
  .feature__label {
    margin: 24px 0 0;
    font-weight: 700;
    font-size: 15.5px;
    line-height: 22px;
    text-shadow: 0 1px 3px rgba(80,20,30,0.45);
  }
  .feature--billing { left: 154px; }
  .feature--relief { left: 381px; }
  .feature--respite { left: 861px; }
  .feature--forms { left: 1066px; }
  .cover__url {
    position: absolute;
    left: 0; right: 0;
    top: 621px;
    text-align: center;
    font-weight: 700;
    font-size: 19px;
    letter-spacing: 6px;
  }
</style>
</head>
<body>
<main class="cover">
  <div class="cover__photo" role="img" aria-label="Foto: Handschlag zwischen einer älteren Person im grauen Strickpullover und einer jüngeren Person im orangefarbenen Pullover, unscharfer Wohnraum im Hintergrund"></div>
  <div class="cover__shade"></div>
  <div class="cover__topbar"></div>

  <header class="brand">
    <span class="brand__dot"></span>
    <span class="brand__name">SONNHAUS</span>
  </header>

  <section class="features">
    <div class="feature feature--billing">
      <svg class="feature__icon" viewBox="0 0 62 58" aria-hidden="true">
        <path d="M12 0h26l12 12v44a2 2 0 0 1-2 2H12a2 2 0 0 1-2-2V2a2 2 0 0 1 2-2z" fill="#fff"/>
        <path d="M38 0v12h12z" fill="#e7a3b0"/>
        <rect x="15" y="10" width="12" height="3" fill="#d56a86"/>
        <rect x="15" y="17" width="8" height="3" fill="#d56a86"/>
        <text x="30" y="49" text-anchor="middle" font-family="Arimo, Arial, sans-serif" font-weight="700" font-size="24" fill="#d56a86">$</text>
      </svg>
      <p class="feature__label">Abrechnung mit allen<br>Pflegekassen möglich</p>
    </div>
    <div class="feature feature--relief">
      <svg class="feature__icon" viewBox="0 0 62 58" aria-hidden="true">
        <path d="M26 0h8v10h10v8H34v10h-8V18H16v-8h10z" fill="#fff"/>
        <path d="M2 42h14c4 0 7 2 9 4h12a3 3 0 0 1 0 6H24v1h14l16-9c3-2 7 1 5 4L44 58H2z" fill="#fff"/>
      </svg>
      <p class="feature__label">Abrechnung über den<br>Entlastungsbetrag</p>
    </div>
    <div class="feature feature--respite">
      <svg class="feature__icon" viewBox="0 0 62 58" aria-hidden="true">
        <path d="M31 28L18 15a8 8 0 0 1 13-10 8 8 0 0 1 13 10z" fill="#fff"/>
        <path d="M2 42h14c4 0 7 2 9 4h12a3 3 0 0 1 0 6H24v1h14l16-9c3-2 7 1 5 4L44 58H2z" fill="#fff"/>
      </svg>
      <p class="feature__label">Auch über die<br>Verhinderungspflege</p>
    </div>
    <div class="feature feature--forms">
      <svg class="feature__icon" viewBox="0 0 62 58" aria-hidden="true">
        <path d="M10 0h26l12 12v44a2 2 0 0 1-2 2H10a2 2 0 0 1-2-2V2a2 2 0 0 1 2-2z" fill="#fff"/>
        <path d="M36 0v12h12z" fill="#e7a3b0"/>
        <path d="M12 46l5-7 4 6 4-4 3 4h6" fill="none" stroke="#d56a86" stroke-width="2.5" stroke-linecap="round"/>
        <path d="M34 44l20-20 6 6-20 20-8 2z" fill="#fff" stroke="#d56a86" stroke-width="2"/>
      </svg>
      <p class="feature__label">Hilfe bei der<br>Antragsstellung</p>
    </div>
  </section>

  <footer class="cover__url">SONNHAUS.DE</footer>
</main>
</body>
</html>
```